依頼詳細
シーズー専門ペットショップ「モフリン」のお客様配布用の2016年 A2版カレンダー作成
記載項目
・作成サイズは 規格A2(420×594ミリ)

・CMYK4色 特色利用不可

・提供された画像をメインにデザインをお願い致します。

・デザインに特に制限はございませんが、明るくかわいらしい感じを希望します。

・「CALENDAR 2016」の様な表記は不要です。

・店舗ロゴ(ワンちゃんの美容室 モフリン・ロゴデータ有)、犬舎名(シーズー専門犬舎 SILVER MEADOW HANAE JP・データ有)、・住所(石川県小松市桜見町丙12-8)・電話(PHONE/FAX 0761-48-5926)、は必ずどこかに入れてください。

・2016年1月から12月までで作成お願いします。なお、カレンダーの玉は、作成者様のお持ちの他データからの流用でも構いませんが、作成者様が校正をお願いします。

・カレンダーの六曜は不要です。
希望イメージ
シンプル 複雑
単色 カラフル
暗い 明るい
日常 高級
遊び心 厳粛
未来的 伝統的
女性的 男性的
希望する色
設定なし
納品ファイル
• 高解像度JPG (.jpg)
• イラストレーター形式 (.ai)
補足説明
最終的な納品時にイラストレータCS2(アウトラインと未アウトライン)形式にて納品いただきます。
また、ご希望される場合、印刷後のカレンダーを数部贈呈いたします。
過去の決定案の画像をアップします。
期間延長いたします。
■ 選んだ理由

可愛らしいデザインが気に入りました。

■ 提案者全員のお礼・コメント

有り難うございます。よかったら来年もご参加お願いします。

```html
<!DOCTYPE html>
<html lang="ja">
<head>
<meta charset="utf-8">
<title>モフリン 2016 カレンダー</title>
<link href="https://fonts.googleapis.com/css2?family=M+PLUS+Rounded+1c:wght@400;700;800&display=swap" rel="stylesheet">
<style>
  :root{
    --pink-deep:#e0456a;
    --pink:#f07f98;
    --pink-soft:#f9d3dc;
    --pink-mist:#fdeef2;
    --cream:#fffbe8;
    --cream-line:#f3e3b8;
    --ink:#4a3a35;
    --holiday:#e03a4e;
    --saturday:#3a6fc4;
    --photo-red:#c8243b;
    --photo-coat:#d9c6b0;
    --white:#ffffff;
  }
  *{box-sizing:border-box;margin:0;padding:0}
  html,body{width:846px;height:1200px;overflow:hidden;background:var(--white)}
  body{font-family:"M PLUS Rounded 1c",sans-serif;color:var(--ink)}
  .calendar-sheet{
    position:relative;width:846px;height:1200px;overflow:hidden;
    background:linear-gradient(to bottom,var(--white) 0%,var(--white) 70%,var(--pink-mist) 86%,var(--pink-soft) 100%);
  }
  .year-title{
    position:absolute;top:6px;left:0;width:100%;height:44px;
    display:flex;align-items:center;justify-content:center;gap:16px;
    color:var(--pink-deep);font-weight:800;font-size:34px;letter-spacing:2px;
  }
  .paw{width:26px;height:26px;fill:var(--pink-deep)}
  .hero-photo{
    position:absolute;top:52px;left:0;width:846px;height:560px;
    background:
      radial-gradient(ellipse 22% 55% at 30% 60%,var(--photo-coat) 0%,rgba(217,198,176,0) 70%),
      radial-gradient(ellipse 22% 55% at 70% 60%,var(--photo-coat) 0%,rgba(217,198,176,0) 70%),
      linear-gradient(to bottom,var(--photo-red) 0%,#e2738a 45%,#f6c9d3 80%,var(--white) 100%);
  }
  .months{
    position:absolute;top:558px;left:22px;width:802px;
    display:grid;grid-template-columns:repeat(4,1fr);column-gap:14px;row-gap:8px;
  }
  .month{
    background:var(--cream);border:1px solid var(--cream-line);border-radius:6px;
    height:168px;padding:6px 10px 4px;opacity:.96;
  }
  .month-name{
    font-weight:800;color:var(--pink);font-size:19px;line-height:22px;margin-bottom:2px;
  }
  .month-name small{font-size:12px;font-weight:700}
  .days{
    display:grid;grid-template-columns:repeat(7,1fr);
    font-size:12px;line-height:22px;text-align:center;font-weight:700;
    border-top:1px solid var(--cream-line);
  }
  .days span{border-bottom:1px dotted var(--cream-line)}
  .days .hol{color:var(--holiday)}
  .days .sat{color:var(--saturday)}
  .shop{
    position:absolute;top:1080px;left:0;width:100%;text-align:center;
  }
  .shop-tag{font-size:12px;font-weight:700;color:var(--pink-deep);letter-spacing:1px}
  .shop-name{
    display:inline-flex;align-items:center;gap:8px;
    font-size:32px;font-weight:800;color:var(--pink-deep);line-height:38px;
  }
  .shop-dot{width:14px;height:14px;border-radius:50%;background:var(--pink-deep)}
  .kennel{font-size:13px;font-weight:700;color:var(--ink);margin-top:4px;letter-spacing:1px}
  .contact{
    font-size:8.5px;color:var(--ink);margin-top:6px;display:flex;justify-content:center;gap:18px;
  }
</style>
</head>
<body>
<main class="calendar-sheet">
  <header class="year-title">
    <svg class="paw" viewBox="0 0 26 26" aria-hidden="true"><ellipse cx="13" cy="17" rx="6.5" ry="5.5"/><circle cx="5" cy="10" r="2.8"/><circle cx="10" cy="5.5" r="2.8"/><circle cx="16" cy="5.5" r="2.8"/><circle cx="21" cy="10" r="2.8"/></svg>
    <span>2016</span>
    <svg class="paw" viewBox="0 0 26 26" aria-hidden="true"><ellipse cx="13" cy="17" rx="6.5" ry="5.5"/><circle cx="5" cy="10" r="2.8"/><circle cx="10" cy="5.5" r="2.8"/><circle cx="16" cy="5.5" r="2.8"/><circle cx="21" cy="10" r="2.8"/></svg>
  </header>

  <div class="hero-photo" role="img" aria-label="赤い背景の前に並んで座る、長い被毛を整えたシーズー2頭の写真"></div>

  <section class="months">
    <article class="month"><h2 class="month-name">1<small>月</small></h2><div class="days">
      <span class="hol" style="grid-column-start:6">1</span><span class="sat">2</span><span class="hol">3</span><span>4</span><span>5</span><span>6</span><span>7</span><span>8</span><span class="sat">9</span><span class="hol">10</span><span class="hol">11</span><span>12</span><span>13</span><span>14</span><span>15</span><span class="sat">16</span><span class="hol">17</span><span>18</span><span>19</span><span>20</span><span>21</span><span>22</span><span class="sat">23</span><span class="hol">24</span><span>25</span><span>26</span><span>27</span><span>28</span><span>29</span><span class="sat">30</span><span class="hol">31</span>
    </div></article>
    <article class="month"><h2 class="month-name">2<small>月</small></h2><div class="days">
      <span style="grid-column-start:2">1</span><span>2</span><span>3</span><span>4</span><span>5</span><span class="sat">6</span><span class="hol">7</span><span>8</span><span>9</span><span>10</span><span class="hol">11</span><span>12</span><span class="sat">13</span><span class="hol">14</span><span>15</span><span>16</span><span>17</span><span>18</span><span>19</span><span class="sat">20</span><span class="hol">21</span><span>22</span><span>23</span><span>24</span><span>25</span><span>26</span><span class="sat">27</span><span class="hol">28</span><span>29</span>
    </div></article>
    <article class="month"><h2 class="month-name">3<small>月</small></h2><div class="days">
      <span style="grid-column-start:3">1</span><span>2</span><span>3</span><span>4</span><span class="sat">5</span><span class="hol">6</span><span>7</span><span>8</span><span>9</span><span>10</span><span>11</span><span class="sat">12</span><span class="hol">13</span><span>14</span><span>15</span><span>16</span><span>17</span><span>18</span><span class="sat">19</span><span class="hol">20</span><span class="hol">21</span><span>22</span><span>23</span><span>24</span><span>25</span><span class="sat">26</span><span class="hol">27</span><span>28</span><span>29</span><span>30</span><span>31</span>
    </div></article>
    <article class="month"><h2 class="month-name">4<small>月</small></h2><div class="days">
      <span style="grid-column-start:6">1</span><span class="sat">2</span><span class="hol">3</span><span>4</span><span>5</span><span>6</span><span>7</span><span>8</span><span class="sat">9</span><span class="hol">10</span><span>11</span><span>12</span><span>13</span><span>14</span><span>15</span><span class="sat">16</span><span class="hol">17</span><span>18</span><span>19</span><span>20</span><span>21</span><span>22</span><span class="sat">23</span><span class="hol">24</span><span>25</span><span>26</span><span>27</span><span>28</span><span class="hol">29</span><span class="sat">30</span>
    </div></article>

    <article class="month"><h2 class="month-name">5<small>月</small></h2><div class="days">
      <span class="hol">1</span><span>2</span><span class="hol">3</span><span class="hol">4</span><span class="hol">5</span><span>6</span><span class="sat">7</span><span class="hol">8</span><span>9</span><span>10</span><span>11</span><span>12</span><span>13</span><span class="sat">14</span><span class="hol">15</span><span>16</span><span>17</span><span>18</span><span>19</span><span>20</span><span class="sat">21</span><span class="hol">22</span><span>23</span><span>24</span><span>25</span><span>26</span><span>27</span><span class="sat">28</span><span class="hol">29</span><span>30</span><span>31</span>
    </div></article>
    <article class="month"><h2 class="month-name">6<small>月</small></h2><div class="days">
      <span style="grid-column-start:4">1</span><span>2</span><span>3</span><span class="sat">4</span><span class="hol">5</span><span>6</span><span>7</span><span>8</span><span>9</span><span>10</span><span class="sat">11</span><span class="hol">12</span><span>13</span><span>14</span><span>15</span><span>16</span><span>17</span><span class="sat">18</span><span class="hol">19</span><span>20</span><span>21</span><span>22</span><span>23</span><span>24</span><span class="sat">25</span><span class="hol">26</span><span>27</span><span>28</span><span>29</span><span>30</span>
    </div></article>
    <article class="month"><h2 class="month-name">7<small>月</small></h2><div class="days">
      <span style="grid-column-start:6">1</span><span class="sat">2</span><span class="hol">3</span><span>4</span><span>5</span><span>6</span><span>7</span><span>8</span><span class="sat">9</span><span class="hol">10</span><span>11</span><span>12</span><span>13</span><span>14</span><span>15</span><span class="sat">16</span><span class="hol">17</span><span class="hol">18</span><span>19</span><span>20</span><span>21</span><span>22</span><span class="sat">23</span><span class="hol">24</span><span>25</span><span>26</span><span>27</span><span>28</span><span>29</span><span class="sat">30</span><span class="hol">31</span>
    </div></article>
    <article class="month"><h2 class="month-name">8<small>月</small></h2><div class="days">
      <span style="grid-column-start:2">1</span><span>2</span><span>3</span><span>4</span><span>5</span><span class="sat">6</span><span class="hol">7</span><span>8</span><span>9</span><span>10</span><span class="hol">11</span><span>12</span><span class="sat">13</span><span class="hol">14</span><span>15</span><span>16</span><span>17</span><span>18</span><span>19</span><span class="sat">20</span><span class="hol">21</span><span>22</span><span>23</span><span>24</span><span>25</span><span>26</span><span class="sat">27</span><span class="hol">28</span><span>29</span><span>30</span><span>31</span>
    </div></article>

    <article class="month"><h2 class="month-name">9<small>月</small></h2><div class="days">
      <span style="grid-column-start:5">1</span><span>2</span><span class="sat">3</span><span class="hol">4</span><span>5</span><span>6</span><span>7</span><span>8</span><span>9</span><span class="sat">10</span><span class="hol">11</span><span>12</span><span>13</span><span>14</span><span>15</span><span>16</span><span class="sat">17</span><span class="hol">18</span><span class="hol">19</span><span>20</span><span>21</span><span class="hol">22</span><span>23</span><span class="sat">24</span><span class="hol">25</span><span>26</span><span>27</span><span>28</span><span>29</span><span>30</span>
    </div></article>
    <article class="month"><h2 class="month-name">10<small>月</small></h2><div class="days">
      <span class="sat" style="grid-column-start:7">1</span><span class="hol">2</span><span>3</span><span>4</span><span>5</span><span>6</span><span>7</span><span class="sat">8</span><span class="hol">9</span><span class="hol">10</span><span>11</span><span>12</span><span>13</span><span>14</span><span class="sat">15</span><span class="hol">16</span><span>17</span><span>18</span><span>19</span><span>20</span><span>21</span><span class="sat">22</span><span class="hol">23</span><span>24</span><span>25</span><span>26</span><span>27</span><span>28</span><span class="sat">29</span><span class="hol">30</span><span>31</span>
    </div></article>
    <article class="month"><h2 class="month-name">11<small>月</small></h2><div class="days">
      <span style="grid-column-start:3">1</span><span>2</span><span class="hol">3</span><span>4</span><span class="sat">5</span><span class="hol">6</span><span>7</span><span>8</span><span>9</span><span>10</span><span>11</span><span class="sat">12</span><span class="hol">13</span><span>14</span><span>15</span><span>16</span><span>17</span><span>18</span><span class="sat">19</span><span class="hol">20</span><span>21</span><span>22</span><span class="hol">23</span><span>24</span><span>25</span><span class="sat">26</span><span class="hol">27</span><span>28</span><span>29</span><span>30</span>
    </div></article>
    <article class="month"><h2 class="month-name">12<small>月</small></h2><div class="days">
      <span style="grid-column-start:5">1</span><span>2</span><span class="sat">3</span><span class="hol">4</span><span>5</span><span>6</span><span>7</span><span>8</span><span>9</span><span class="sat">10</span><span class="hol">11</span><span>12</span><span>13</span><span>14</span><span>15</span><span>16</span><span class="sat">17</span><span class="hol">18</span><span>19</span><span>20</span><span>21</span><span>22</span><span class="hol">23</span><span class="sat">24</span><span class="hol">25</span><span>26</span><span>27</span><span>28</span><span>29</span><span>30</span><span class="sat">31</span>
    </div></article>
  </section>

  <footer class="shop">
    <p class="shop-tag">ワンちゃんの美容室</p>
    <p class="shop-name"><span class="shop-dot"></span>モフリン</p>
    <p class="kennel">シーズー専門犬舎 SILVER MEADOW HANAE JP</p>
    <p class="contact">
      <span>石川県小松市桜見町丙12-8</span>
      <span>PHONE/FAX 0761-48-5926</span>
      <span>営業時間 10:00〜18:00</span>
      <span>mofurin-shihtzu.example</span>
    </p>
  </footer>
</main>
</body>
</html>
```